Postcard Design

www.tovil.com.au
i am an occupational therapist and professionally trained coach. i work with children, parents and disability service providers to achieve brilliant outcomes for children with special needs.
http://www.tovil.com.au/service/for-families
I need a postcard to give parents to promote our family service coaching service
A family service coach will work with you to set specific goals for your child, build a dream team, design and manage your child's highly effective therapy and educational team to ensure brilliant outcomes for your child..
KORBU - you have done my business card previously. they were great thank you.

```html
<!DOCTYPE html>
<html lang="en">
<head>
<meta charset="utf-8">
<title>Tovil Family Service Coaching Postcard</title>
<link rel="stylesheet" href="https://fonts.googleapis.com/css2?family=Open+Sans:wght@300;400;700&display=swap">
<style>
  :root {
    --backdrop: #e4e6e8;
    --card: #ffffff;
    --brand-blue: #5b7fb5;
    --brand-teal: #68c2b8;
    --postage-fill: #ececec;
    --postage-text: #ffffff;
    --ink-light: #ffffff;
    --photo-dark: #4d5d70;
    --photo-mid: #6f7f90;
    --photo-warm: #b88d78;
  }
  * { margin: 0; padding: 0; box-sizing: border-box; }
  html, body {
    width: 1200px;
    height: 800px;
    overflow: hidden;
    background: var(--backdrop);
    font-family: "Open Sans", Arial, sans-serif;
  }
  .postcard {
    position: absolute;
    left: 151px;
    top: 55px;
    width: 897px;
    height: 690px;
    background: var(--card);
    box-shadow: 0 2px 8px rgba(0,0,0,0.18);
  }
  .top-band {
    position: absolute;
    left: 52px; top: 0;
    width: 419px; height: 51px;
    background: var(--brand-blue);
  }
  .feature-photo {
    position: absolute;
    left: 52px; top: 51px;
    width: 419px; height: 587px;
    background:
      radial-gradient(ellipse at 55% 45%, rgba(184,141,120,0.55), transparent 60%),
      linear-gradient(160deg, var(--photo-mid) 0%, var(--photo-dark) 100%);
  }
  .brand {
    position: absolute;
    left: 79px; top: 357px;
    display: flex;
    align-items: center;
    gap: 18px;
    color: var(--ink-light);
  }
  .brand-dot {
    width: 58px; height: 58px;
    border-radius: 50%;
    background: var(--ink-light);
  }
  .brand-name {
    font-weight: 700;
    font-size: 60px;
    line-height: 1;
    letter-spacing: -1px;
  }
  .contact {
    position: absolute;
    left: 76px; top: 455px;
    color: var(--ink-light);
  }
  .contact-name {
    font-size: 24px;
    font-weight: 400;
    line-height: 30px;
    margin-bottom: 6px;
  }
  .contact-role {
    font-size: 17px;
    font-weight: 300;
    line-height: 24px;
    margin-bottom: 27px;
  }
  .contact-line {
    font-size: 17px;
    font-weight: 300;
    line-height: 25px;
  }
  .contact-line strong { font-weight: 400; }
  .postage-area {
    position: absolute;
    left: 680px; top: 12px;
    width: 204px; height: 205px;
    background: var(--postage-fill);
    color: var(--postage-text);
    font-size: 24px;
    font-weight: 400;
    line-height: 32px;
    text-align: center;
    padding-top: 82px;
  }
  .bottom-square {
    position: absolute;
    left: 0; top: 638px;
    width: 52px; height: 52px;
    background: var(--brand-blue);
  }
  .bottom-band {
    position: absolute;
    left: 52px; top: 638px;
    width: 845px; height: 52px;
    background: var(--brand-teal);
  }
</style>
</head>
<body>
  <main class="postcard">
    <div class="top-band"></div>
    <div class="feature-photo" role="img" aria-label="Photo of several hands joining colourful jigsaw puzzle pieces against a grey-blue background"></div>

    <div class="brand">
      <span class="brand-dot"></span>
      <span class="brand-name">tovil</span>
    </div>

    <div class="contact">
      <p class="contact-name">Mara Quill</p>
      <p class="contact-role">Occupational Therapist Coach,<br>Speaker and Author</p>
      <p class="contact-line">Email <strong>mara@tovil.com.au</strong></p>
      <p class="contact-line">Mobile <strong>0400 555 218</strong></p>
    </div>

    <div class="postage-area">Postage<br>Area</div>

    <div class="bottom-square"></div>
    <div class="bottom-band"></div>
  </main>
</body>
</html>
```